Stationery Design Project

Brisk-Span Consultants is interim management company. We are specialized in finding the best Finance and IT consultants for our clients when they require additional resources on an interim basis for projects or special situations. We are flexible in our approach and we always seek to maximize the benefits for our clients as well as our consultants.

We are looking for a design of our letterhead, general stationery and business cards using the company name. The design will also be found on our coming web pages.
Updates

Please also create a logo for Brisk-Span Consultants which expresses that we want to match the best finance and IT people to our customers projects

Target Market(s)

Larger and mid sized companies (all sectors), as well as highly skilled Finance & IT professionals/consultants

Industry/Entity Type

Business

Requirements
Must have
• Brisk-Span Consultants
We are expecting that 'Brisk-Span' will be on the first line and 'Consultants' on a second line.
Please also indicate style of the letters for our address/phone and mail details. Our current address is:
Tornagervej 14,
2915 Skovlunde
Danmark
Mobile: +45 XX XX XX XX Mail: xx@brisk-span.dk

```html
<!DOCTYPE html>
<html lang="en">
<head>
<meta charset="utf-8">
<title>Brisk-Span Consultants — Stationery</title>
<link href="https://fonts.googleapis.com/css2?family=Tinos:wght@400;700&display=swap" rel="stylesheet">
<style>
  :root {
    --backdrop: #5f5f5f;
    --brand-red: #e32526;
    --ink-grey: #58595b;
    --mark-grey: #5a5a5c;
    --card-light: #f4f4f4;
    --card-edge: #d8d8d8;
    --paper: #ffffff;
    --serif: "Tinos", "Times New Roman", serif;
  }
  * { margin: 0; padding: 0; box-sizing: border-box; }
  html, body {
    width: 1200px; height: 2618px; overflow: hidden;
    background: var(--backdrop);
    font-family: var(--serif);
    color: var(--ink-grey);
  }
  .sheet { position: absolute; left: 100px; width: 984px; overflow: hidden; }
  .card {
    height: 561px;
    background: radial-gradient(ellipse at 45% 40%, var(--card-light) 0%, #ececec 45%, var(--card-edge) 100%);
  }
  .card--front { top: 22px; }
  .card--back { top: 611px; }
  .letterhead { top: 1196px; height: 1394px; background: var(--paper); }

  .brand { position: absolute; display: flex; align-items: center; }
  .brand__square { background: var(--mark-grey); flex: none; }
  .brand__name {
    color: var(--brand-red); font-weight: 400; line-height: 1;
    text-transform: uppercase;
  }
  .brand__line { display: block; }
  .brand__line--sub { letter-spacing: 0.42em; }

  .card--front .brand { left: 162px; top: 185px; }
  .card--front .brand__square { width: 163px; height: 163px; margin-right: 28px; }
  .card--front .brand__line--main { font-size: 80px; }
  .card--front .brand__line--sub { font-size: 27px; margin-top: 6px; padding-left: 170px; }

  .brand--small .brand__square { width: 107px; height: 107px; margin-right: 18px; }
  .brand--small .brand__line--main { font-size: 52px; }
  .brand--small .brand__line--sub { font-size: 18px; margin-top: 4px; padding-left: 112px; }
  .card--back .brand { left: 70px; top: 55px; }
  .letterhead .brand { left: 68px; top: 76px; }

  .web {
    position: absolute; left: 0; right: 0; text-align: center;
    font-size: 30px; letter-spacing: 0.28em; color: var(--ink-grey);
  }
  .web__name { color: var(--brand-red); }
  .card--front .web { top: 462px; }
  .letterhead .web { top: 1338px; }

  .contact { position: absolute; font-size: 24px; line-height: 27px; color: var(--ink-grey); }
  .contact__label { color: var(--brand-red); }
  .card--back .contact { left: 597px; top: 326px; }
  .contact__person { color: var(--brand-red); font-size: 30px; line-height: 34px; }
  .contact__role { font-size: 23px; margin-bottom: 22px; }

  .letterhead__rule {
    position: absolute; left: 617px; top: 83px; width: 2px; height: 92px;
    background: var(--brand-red);
  }
  .letterhead .contact { left: 637px; top: 84px; font-size: 22px; line-height: 25px; }
</style>
</head>
<body>

<section class="sheet card card--front">
  <div class="brand">
    <span class="brand__square"></span>
    <span class="brand__name">
      <span class="brand__line brand__line--main">Brisk-Span</span>
      <span class="brand__line brand__line--sub">Consultants</span>
    </span>
  </div>
  <p class="web">WWW.<span class="web__name">BRISK-SPAN</span>.DK</p>
</section>

<section class="sheet card card--back">
  <div class="brand brand--small">
    <span class="brand__square"></span>
    <span class="brand__name">
      <span class="brand__line brand__line--main">Brisk-Span</span>
      <span class="brand__line brand__line--sub">Consultants</span>
    </span>
  </div>
  <address class="contact" style="font-style:normal">
    <div class="contact__person">Consultant Name</div>
    <div class="contact__role">Position</div>
    <div>Tornagervej 14,</div>
    <div>2915 Skovlunde, Danmark</div>
    <div><span class="contact__label">Mobile:</span> + 45 XX XX XX XX</div>
    <div><span class="contact__label">Email:</span> xx@brisk-span.dk</div>
    <div><span class="contact__label">Website:</span> www.brisk-span.dk</div>
  </address>
</section>

<section class="sheet letterhead">
  <div class="brand brand--small">
    <span class="brand__square"></span>
    <span class="brand__name">
      <span class="brand__line brand__line--main">Brisk-Span</span>
      <span class="brand__line brand__line--sub">Consultants</span>
    </span>
  </div>
  <span class="letterhead__rule"></span>
  <address class="contact" style="font-style:normal">
    <div>Tornagervej 14,</div>
    <div>2915 Skovlunde, Danmark</div>
    <div><span class="contact__label">Mobile:</span> + 45 XX XX XX XX</div>
    <div><span class="contact__label">Email:</span> xx@brisk-span.dk</div>
  </address>
  <p class="web">WWW.<span class="web__name">BRISK-SPAN</span>.DK</p>
</section>

</body>
</html>
```